Quiet Harbor Lane - The best guide in your pocket

Quiet Harbor Lane (آبیکوهستانها in Persian)

We need a new app design for a major update on Android, iOS and Windows Universal platforms.
Our company works on creating innovative apps and games on different platforms, this particular app is free for end users and provides location based services. Here is the abstract feature list:
• Nearest points around user (explore on map or find) including locations, events and skills
• Add points to our database (partners) plus comments and ratings
• Point owners can modify or complete their points data, provide sale events, services and …

Attachments:
Our service logo
The detailed descriptions of different sections (PDF documents)
Updates

Project Deadline Extended Reason: We want more designs :)Give us previews on Home and Map sections at least (more interesting if previews are provided for more sections) Added Saturday, January 7, 2017

Target Market(s)

Public

Industry/Entity Type

Android

Font styles to use
Serif
Sans Serif

Requirements
Must have
• Consider attached service logo & wireframe
• Designs for attached sections
• Fluent user experience
• Modern design
Nice to have
• Right to Left layouts
Should not have
• No alphabet in graphic assets

```html
<!DOCTYPE html>
<html lang="en">
<head>
<meta charset="utf-8">
<title>Profile – General data</title>
<link rel="stylesheet" href="https://fonts.googleapis.com/css2?family=Roboto:wght@300;400;500&display=swap">
<style>
  :root {
    --status-bg: #344b58;
    --header-bg: #486a7c;
    --tab-muted: #7f9aa9;
    --white: #ffffff;
    --page-bg: #f2f2f2;
    --field-bg: #ffffff;
    --placeholder: #9a9a9a;
    --teal: #7dc9c3;
    --teal-shadow: #68b2ac;
    --icon-dark: #466878;
    --media-bg: #dfdfdf;
    --media-icon: #d0d0d0;
    --avatar-bg: #cccccc;
  }
  * { box-sizing: border-box; margin: 0; padding: 0; }
  html, body { width: 674px; height: 1200px; overflow: hidden; }
  body {
    position: relative;
    background: var(--page-bg);
    font-family: "Roboto", sans-serif;
  }
  .status-bar {
    position: absolute; left: 0; top: 0; width: 674px; height: 45px;
    background: var(--status-bg); color: var(--white);
    font-size: 23px; font-weight: 300;
  }
  .status-bar .carrier { position: absolute; left: 14px; top: 9px; display: flex; align-items: center; gap: 6px; }
  .status-bar .time { position: absolute; left: 0; right: 0; top: 8px; text-align: center; font-weight: 400; }
  .status-bar .battery { position: absolute; right: 12px; top: 9px; display: flex; align-items: center; gap: 8px; }
  .app-header {
    position: absolute; left: 0; top: 45px; width: 674px; height: 118px;
    background: var(--header-bg);
    box-shadow: 0 2px 3px rgba(0,0,0,0.15);
  }
  .app-header .title {
    position: absolute; left: 22px; top: 18px;
    color: var(--white); font-size: 24px; font-weight: 500;
  }
  .tabs .tab {
    position: absolute; top: 65px; font-size: 22px; font-weight: 500; color: var(--tab-muted);
  }
  .tabs .tab.active { color: var(--white); }
  .tabs .indicator {
    position: absolute; left: 0; bottom: 0; width: 225px; height: 5px; background: var(--white);
  }
  .avatar { position: absolute; left: 256px; top: 196px; }
  .field {
    position: absolute; left: 52px; width: 570px; height: 80px;
    background: var(--field-bg);
    box-shadow: 0 1px 2px rgba(0,0,0,0.25);
    display: flex; align-items: center;
  }
  .field .field-icon { width: 78px; height: 80px; flex: none; }
  .field .label { margin-left: 23px; font-size: 25px; color: var(--placeholder); }
  .media-slot {
    position: absolute; left: 52px; top: 617px; width: 570px; height: 293px;
    background: var(--media-bg);
    box-shadow: 0 1px 2px rgba(0,0,0,0.2);
  }
</style>
</head>
<body>
  <div class="status-bar">
    <div class="carrier">
      <svg width="72" height="16" viewBox="0 0 72 16">
        <g fill="#fff"><circle cx="7" cy="8" r="6"/><circle cx="21" cy="8" r="6"/><circle cx="35" cy="8" r="6"/></g>
        <g fill="none" stroke="#fff" stroke-width="1.2"><circle cx="49" cy="8" r="5.4"/><circle cx="63" cy="8" r="5.4"/></g>
      </svg>
      <span>MAPLE</span>
      <svg width="22" height="16" viewBox="0 0 22 16" fill="none" stroke="#fff" stroke-width="2.4" stroke-linecap="round">
        <path d="M2 6 Q11 -2 20 6"/><path d="M5.5 9.5 Q11 4.5 16.5 9.5"/><circle cx="11" cy="13.5" r="1.6" fill="#fff" stroke="none"/>
      </svg>
    </div>
    <div class="time">4:21 PM</div>
    <div class="battery">
      <span>100%</span>
      <svg width="50" height="22" viewBox="0 0 50 22">
        <rect x="1" y="2" width="44" height="18" rx="3" fill="none" stroke="#fff" stroke-width="1.5"/>
        <rect x="3.5" y="4.5" width="39" height="13" rx="1.5" fill="#fff"/>
        <rect x="46" y="8" width="3" height="6" rx="1" fill="#fff"/>
      </svg>
    </div>
  </div>

  <header class="app-header">
    <div class="title">Profile</div>
    <nav class="tabs">
      <span class="tab active" style="left:28px">General data</span>
      <span class="tab" style="left:274px">Finacial data</span>
      <span class="tab" style="left:512px">Pointowner</span>
      <span class="indicator"></span>
    </nav>
  </header>

  <svg class="avatar" width="164" height="164" viewBox="0 0 164 164" aria-label="Profile photo placeholder">
    <defs>
      <clipPath id="avatar-clip"><circle cx="82" cy="82" r="74"/></clipPath>
    </defs>
    <circle cx="82" cy="84" r="81" fill="rgba(0,0,0,0.12)"/>
    <circle cx="82" cy="82" r="81" fill="var(--white)"/>
    <circle cx="82" cy="82" r="74" fill="var(--avatar-bg)"/>
    <g clip-path="url(#avatar-clip)" fill="var(--white)">
      <path d="M82 20 C104 20 113 36 112 54 C111 70 104 80 101 88 L103 113 C120 120 138 126 150 136 L150 170 L14 170 L14 136 C26 126 44 120 61 113 L63 88 C60 80 53 70 52 54 C51 36 60 20 82 20 Z"/>
    </g>
  </svg>

  <div class="field" style="top:398px">
    <svg class="field-icon" viewBox="0 0 78 80">
      <rect width="78" height="80" fill="var(--teal)"/>
      <polygon points="40,28 78,66 78,80 60,80 28,48 40,40" fill="var(--teal-shadow)"/>
      <g fill="var(--icon-dark)">
        <circle cx="39" cy="31" r="8"/>
        <path d="M25 56 C25 45 31 41 39 41 C47 41 53 45 53 56 Z"/>
      </g>
    </svg>
    <span class="label">first name</span>
  </div>

  <div class="field" style="top:501px">
    <svg class="field-icon" viewBox="0 0 78 80">
      <rect width="78" height="80" fill="var(--teal)"/>
      <polygon points="40,28 78,66 78,80 60,80 28,48 40,40" fill="var(--teal-shadow)"/>
      <g fill="var(--icon-dark)">
        <circle cx="39" cy="31" r="8"/>
        <path d="M25 56 C25 45 31 41 39 41 C47 41 53 45 53 56 Z"/>
      </g>
    </svg>
    <span class="label">Last name</span>
  </div>

  <div class="media-slot" role="img" aria-label="Business photo upload area">
    <svg width="570" height="293" viewBox="0 0 570 293">
      <g fill="var(--media-icon)">
        <path d="M182 81 L200 81 L200 230 L362 230 L362 243 L182 244 Z"/>
        <rect x="209" y="55" width="180" height="157" rx="3"/>
      </g>
      <g fill="var(--media-bg)">
        <circle cx="257" cy="87" r="19"/>
        <polygon points="221,167 251,131 271,143 290,109 312,129 335,84 377,167"/>
      </g>
    </svg>
  </div>

  <div class="field" style="top:943px">
    <svg class="field-icon" viewBox="0 0 78 80">
      <rect width="78" height="80" fill="var(--teal)"/>
      <polygon points="54,26 78,50 78,80 60,80 26,46 26,54 54,54" fill="var(--teal-shadow)"/>
      <g fill="var(--icon-dark)">
        <rect x="25" y="26" width="13" height="13"/>
        <rect x="40" y="26" width="13" height="13"/>
        <rect x="25" y="41" width="13" height="13"/>
        <rect x="40" y="41" width="13" height="13"/>
      </g>
    </svg>
    <span class="label">Business category name</span>
  </div>
</body>
</html>
```